New Website Design for Sola Brisa Coffee

Need a website design to be uploaded on Cartwell.com. Here are some of the sites I like:
https://grindlet.example
https://www.ridgecrowcoffee.example
https://hallowbrew.example

```html
<!DOCTYPE html>
<html lang="en">
<head>
<meta charset="utf-8">
<title>Sola Brisa Coffee</title>
<link href="https://fonts.googleapis.com/css2?family=Josefin+Sans:wght@300;400;600&family=Playfair+Display:wght@400;500&display=swap" rel="stylesheet">
<style>
:root{
  --stage:#e8d8ce;
  --peach:#eeb29a;
  --peach-foot:#eeaa90;
  --cream:#f7eee6;
  --charcoal:#333232;
  --espresso:#3e2f21;
  --roast:#5c4530;
  --copper:#b9826a;
  --caramel:#c68a62;
  --ink:#3a302b;
  --line:#d9c6b8;
  --white:#ffffff;
}
*{box-sizing:border-box;margin:0;padding:0}
html,body{width:1200px;height:2551px;overflow:hidden;background:var(--stage)}
body{position:relative;font-family:"Josefin Sans",sans-serif;color:var(--ink)}
.page{position:absolute;left:308px;top:33px;width:596px;height:2510px;background:var(--cream)}
.abs{position:absolute}
.serif{font-family:"Playfair Display",serif}
section{position:absolute;left:0;width:596px}

/* hero */
.hero{top:0;height:333px;background:var(--peach);color:var(--white)}
.hero .menu{left:45px;top:24px;width:12px}
.hero .menu span{display:block;height:1px;background:var(--white);margin-bottom:3px}
.hero .menu span:last-child{width:8px}
.hero .brand{left:72px;top:22px;font-size:10px;letter-spacing:.3px}
.hero .nav{top:24px;font-size:5px}
.hero .shop-box{left:498px;top:7px;width:52px;height:272px;border:1px solid rgba(255,255,255,.8)}
.hero .shop-text{left:14px;top:60px;width:20px;height:160px;writing-mode:vertical-rl;transform:rotate(180deg);font-size:11px;letter-spacing:5px;text-align:center}
.hero .dots{left:10px;top:250px;display:flex;gap:7px}
.hero .dots i{width:5px;height:5px;border-radius:50%;background:var(--white);display:block}
.hero .title{left:0;width:596px;top:42px;text-align:center;font-size:52px;line-height:1;letter-spacing:-1px;transform:scaleX(.82)}
.hero .subtitle{left:0;width:596px;top:103px;text-align:center;font-size:9px;letter-spacing:.5px}
.hero .still{left:112px;top:117px;width:290px;height:170px;border-radius:40px;background:radial-gradient(ellipse at 55% 40%,#fbe9dd 0 18%,#f2c0a8 40%,var(--peach) 72%)}
.hero .cta{left:255px;top:295px;width:87px;height:23px;background:#fbe3d4;color:var(--ink);font-size:5.5px;display:flex;align-items:center;justify-content:center;letter-spacing:.4px;border-radius:2px}
.hero .phone{right:46px;top:304px;font-size:5.5px}

/* organic */
.organic{top:333px;height:404px;background:var(--cream)}
.organic .panel{left:0;top:0;width:412px;height:404px;background:var(--charcoal);color:var(--white)}
.organic h2{left:78px;top:84px;font-size:38px;line-height:41px;font-weight:400;transform:scaleX(.85);transform-origin:left}
.organic p{left:78px;width:182px;font-size:6.5px;line-height:10.7px;font-weight:300}
.btn-solid{background:var(--copper);color:var(--white);font-size:5.5px;display:flex;align-items:center;justify-content:center;border-radius:2px;letter-spacing:.4px}
.organic .beans{left:312px;top:231px;width:218px;height:116px;background:linear-gradient(120deg,#f6ede3,#eadccd 50%,#f6ede3)}

/* story */
.story{top:737px;height:366px;background:var(--cream)}
.story .sketch{left:64px;top:60px;width:203px;height:215px;background:radial-gradient(ellipse at 50% 55%,#e4d8cd,var(--cream) 70%)}
.story .label{left:307px;top:69px;font-size:6px;letter-spacing:.3px}
.story p{left:307px;width:240px;font-size:7px;line-height:12.5px;font-weight:300}
.story .tags{left:307px;top:174px;font-size:6px;display:flex;gap:12px}
.btn-line{border:1px solid var(--copper);color:var(--ink);font-size:5.5px;display:flex;align-items:center;justify-content:center;border-radius:3px;letter-spacing:.3px}

/* product */
.product{top:1103px;height:304px;background:var(--cream)}
.product .photo{left:0;top:0;width:333px;height:304px;background:linear-gradient(var(--espresso) 0 151px,var(--roast) 151px)}
.product .bag{left:77px;top:59px;width:135px;height:225px;background:linear-gradient(160deg,#e6dbc4,#c9b99a)}
.product .arrow{left:282px;top:6px;width:33px;height:33px;border:1px solid #c9b5a0;border-radius:50%}
.spec{left:334px;top:0;width:217px;height:304px}
.spec .cell{position:absolute;border:1px solid var(--line)}
.spec .small{font-size:5px}
.spec .desc{left:8px;top:114px;width:204px;font-size:6px;line-height:10.7px;font-weight:300}
.spec .desc em{font-style:normal;color:var(--caramel)}
.spec .col{top:209px;height:60px;width:73px;padding:6px 7px}
.spec .col b{display:block;font-size:5.5px;font-weight:600;margin-bottom:5px;letter-spacing:.3px}
.spec .col span{font-size:5px;line-height:8.7px;font-weight:300;display:block}

/* collections & stats */
.collections{top:1407px;height:266px;background:var(--cream)}
.collections .rule{top:0;width:1px;height:62px;background:var(--line)}
.tabs{left:45px;top:62px;width:376px;height:36px;display:flex}
.tabs div{flex:1;border:1px solid var(--line);display:flex;align-items:center;justify-content:center;font-size:8.5px;font-weight:300}
.tabs div+div{border-left:none}
.stat{width:160px;text-align:center;color:var(--caramel)}
.stat .num{font-size:40px;line-height:1}
.stat .cap{font-size:10px;font-weight:300;margin-top:14px}

/* shipping band */
.band{top:1673px;height:335px;background:radial-gradient(ellipse at 60% 55%,#5a4232,#2e2620 70%)}
.band .text{left:45px;top:127px;color:#efe5dc;font-size:12px;line-height:20px;font-weight:300}
.band .play{left:45px;top:180px;width:23px;height:23px}

/* testimonials */
.testimonials{top:2008px;height:336px;background:var(--cream)}
.testimonials .garden{left:45px;top:32px;width:223px;height:272px;background:linear-gradient(160deg,#6f7a4a,#a9ae7c 45%,#e6dcbc 70%,#59633a)}
.quote-box{left:328px;top:32px;width:223px;height:224px;background:var(--charcoal);color:#eee}
.quote-box .vlabel{left:104px;top:7px;writing-mode:vertical-rl;transform:rotate(180deg);font-size:8px;letter-spacing:1px}
.quote-box .quote{left:40px;top:117px;width:143px;text-align:center;font-size:8.5px;line-height:12.3px;font-weight:300}
.testimonials .rule{left:274px;top:294px;width:133px;height:1px;background:var(--line)}
.testimonials .name{left:415px;top:289px;font-size:8px;font-weight:300}

/* footer */
.footer{top:2344px;height:166px;background:var(--peach-foot);color:var(--white)}
.footer .brand{left:82px;top:49px;font-size:10px}
.footer .about{left:82px;top:75px;width:160px;font-size:4.5px;line-height:11px;font-weight:300}
.footer .copy{left:82px;top:110px;font-size:4.5px;font-weight:300}
.footer .col{top:49px;font-size:4.5px;font-weight:300}
.footer .col b{display:block;font-size:6px;font-weight:600;margin-bottom:8px}
.footer .col span{display:block;line-height:11px}
</style>
</head>
<body>
<div class="page">

  <section class="hero">
    <div class="abs menu"><span></span><span></span></div>
    <div class="abs brand">Sola Brisa</div>
    <div class="abs nav" style="left:472px">Login</div>
    <div class="abs nav" style="left:504px">Add to Cart</div>
    <svg class="abs" style="left:537px;top:22px" width="8" height="8" viewBox="0 0 8 8" fill="none" stroke="#fff" stroke-width=".7"><path d="M.5 1h1.2l1 4h4l.8-3H2"/><circle cx="3.2" cy="6.6" r=".5"/><circle cx="6" cy="6.6" r=".5"/></svg>
    <div class="abs shop-box">
      <div class="abs shop-text">SHOP ONLINE</div>
      <div class="abs dots"><i></i><i></i><i></i></div>
    </div>
    <h1 class="abs title serif" style="font-weight:400">Good Morning</h1>
    <div class="abs subtitle">Black coffee and latte 2x1</div>
    <div class="abs still" role="img" aria-label="Top view of a latte cup on a saucer with a white chrysanthemum and pink flower sprigs"></div>
    <div class="abs cta">SEE MORE</div>
    <div class="abs phone">+ 01 800 55501234</div>
  </section>

  <section class="organic">
    <div class="abs panel">
      <h2 class="abs serif">Organic<br>Coffee</h2>
      <p class="abs" style="top:180px">Lorem ipsum dolor sit amet, consectetuer adipiscing elit, sed diam nonummy nibh euismod tincidunt ut laoreet dolore magna aliquam erat volutpat.</p>
      <p class="abs" style="top:223px">Lorem ipsum dolor sit amet, consectetuer adipiscing elit, sed diam nonummy nibh euismod tincidunt ut laoreet dolore magna.</p>
      <div class="abs btn-solid" style="left:78px;top:281px;width:87px;height:23px">SEE MORE</div>
    </div>
    <div class="abs beans" role="img" aria-label="Ink sketch of roasted coffee beans with light watercolour splashes"></div>
  </section>

  <section class="story">
    <div class="abs sketch" role="img" aria-label="Ink sketch of a moka pot beside a steaming cup on a saucer with scattered beans"></div>
    <div class="abs label">SOLA BRISA'S STORY</div>
    <p class="abs" style="top:86px">Lorem ipsum dolor sit amet, consectetuer adipiscing elit, sed diam nonummy nibh euismod tincidunt ut laoreet dolore magna aliquam erat volutpat.</p>
    <p class="abs" style="top:136px">Lorem ipsum dolor sit amet, consectetuer adipiscing elit, sed diam nonummy nibh euismod tincidunt ut laoreet dolore magna.</p>
    <div class="abs tags"><span>All Natural</span><span>|</span><span>No Chemical Essence</span></div>
    <div class="abs btn-line" style="left:307px;top:221px;width:88px;height:23px">READ MORE</div>
  </section>

  <section class="product">
    <div class="abs photo">
      <div class="abs bag" role="img" aria-label="Paper coffee bag with vintage print standing on a bed of roasted beans"></div>
      <svg class="abs arrow" viewBox="0 0 33 33" fill="none" stroke="#e6d6c6" stroke-width="1"><path d="M14.5 11l5 5.5-5 5.5"/></svg>
    </div>
    <div class="abs spec">
      <div class="cell" style="left:0;top:0;width:217px;height:304px"></div>
      <div class="cell" style="left:0;top:0;width:42px;height:65px"></div>
      <div class="abs small" style="left:3px;top:30px">Black Coffee</div>
      <div class="cell" style="left:0;top:64px;width:42px;height:46px"></div>
      <div class="abs" style="left:0;top:79px;width:42px;text-align:center;font-size:9px">80<br><span style="font-size:4.5px;display:block;margin-top:-2px">Kg</span></div>
      <div class="cell" style="left:41px;top:0;width:135px;height:110px"></div>
      <div class="abs serif" style="left:41px;top:20px;width:135px;text-align:center;font-size:18px;line-height:24px">Flavour<br>Name<br>Here</div>
      <div class="cell" style="left:175px;top:0;width:42px;height:35px"></div>
      <div class="abs small" style="left:180px;top:14px;color:#a99">Out of Stock</div>
      <div class="cell" style="left:175px;top:74px;width:42px;height:36px"></div>
      <div class="abs small" style="left:181px;top:89px;color:var(--caramel)">View More</div>
      <div class="abs desc">Lorem ipsum dolor sit amet, consectetuer adipiscing elit, sed diam nonummy nibh euismod tincidunt ut laoreet dolore magna aliquam erat volutpat.<br>Lorem ipsum dolor sit amet, consectetuer adipiscing elit, sed diam nonummy nibh euismod tincidunt ut laoreet dolore magna. Lorem ipsum dolor sit amet, consectetuer adipiscing elit, sed diam nonummy nibh euismod tincidunt ut laoreet dolore magna aliquam erat volutpat. <em>Read More</em></div>
      <div class="cell col" style="left:0"><b>TASTE</b><span>Lorem ipsum dolor sit amet, consectetuer adipiscing elit, sed diam nonummy nibh</span></div>
      <div class="cell col" style="left:72px"><b>AROMA</b><span>Lorem ipsum dolor sit amet, consectetuer adipiscing elit, sed diam nonummy nibh</span></div>
      <div class="cell col" style="left:144px"><b>MOUTHFEEL</b><span>Lorem ipsum dolor sit amet, consectetuer adipiscing elit, sed diam nonummy nibh</span></div>
      <div class="abs serif" style="left:8px;top:274px;font-size:16px"><sup style="font-size:6px">$</sup>/00.00</div>
      <div class="abs btn-line" style="left:123px;top:275px;width:88px;height:21px;border-color:var(--line)">Add to Cart</div>
    </div>
  </section>

  <section class="collections">
    <div class="abs rule" style="left:107px"></div>
    <div class="abs rule" style="left:358px"></div>
    <div class="abs tabs"><div>Coffee Collection</div><div>Upcoming Items</div><div>Discount On</div></div>
    <div class="abs stat" style="left:12px;top:165px"><div class="num serif">250</div><div class="cap">Varieties of coffee</div></div>
    <div class="abs stat" style="left:228px;top:165px"><div class="num serif">520</div><div class="cap">Coffee Markets</div></div>
    <div class="abs stat" style="left:434px;top:165px"><div class="num serif">123</div><div class="cap">Coffee Brands</div></div>
  </section>

  <section class="band" role="img" aria-label="Dim café interior with baristas working behind a wooden counter">
    <div class="abs text">FREE SHIPPING ON COFFEE<br>ORDERS OVER $50!</div>
    <svg class="abs play" viewBox="0 0 23 23" fill="none" stroke="#efe5dc" stroke-width=".8"><circle cx="11.5" cy="11.5" r="11"/><path d="M9.5 8v7l5.5-3.5z"/></svg>
  </section>

  <section class="testimonials">
    <div class="abs garden" role="img" aria-label="Mother and daughter among cream rose bushes in a garden"></div>
    <div class="abs quote-box">
      <div class="abs vlabel">TESTIMONIALS</div>
      <div class="abs quote">"Lorem ipsum dolor sit amet, consectetuer adipiscing elit, sed diam nonummy nibh euismod tincidunt ut laoreet dolore magna."</div>
    </div>
    <div class="abs rule"></div>
    <div class="abs name">Mara Ellison</div>
  </section>

  <footer class="abs footer" style="left:0;width:596px">
    <div class="abs brand">Sola Brisa.</div>
    <div class="abs about">We are a shop located in different parts of the world.<br>Our team is working from New York and London.</div>
    <div class="abs copy">Copyright 2020 - 2025 Sola Brisa. All Rights Reserved.</div>
    <div class="abs col" style="left:298px"><b>About Us</b><span>Our Blog</span><span>Careers</span><span>News</span><span>Help Center</span></div>
    <div class="abs col" style="left:385px"><b>Products</b><span>Black Coffee</span><span>Americano</span><span>Green Tea</span><span>Chai Latte</span></div>
    <div class="abs col" style="left:472px"><b>Contact</b><span>The Team</span><span>NY Shop</span><span>London Shop</span><span>Help Center</span></div>
  </footer>

</div>
</body>
</html>
```